New Packaging and label for New Beard Oil and Shampoo brand from London

Oils, Shampoo ect .. Beard Oil Ingredients: Application Directions: Apply to beard by weight in a small amount of oil will naturally absorb. Leaving it soft & conditioned. Ingredients: Coconut oil, scented oil, Oud oil, vitamin E 100% Natural `i will have 5 types of oils Vanilla Oud Rose Oud Cocktail Tea tree Velvet Dusk

Target Market(s)

A fashionable well groomed professional gentleman who is willing to invest in his appearance.

Industry/Entity Type

It Company

Font styles to use
Sans Serif

Colors

Designer to choose colors to be used in the design.

Requirements
Must have
• Beard Oil Ingredients: Application Directions: Apply to a beard by a small amount of oil will naturally absorb. Leaving it soft & conditioned. Ingredients: Coconut Oil, Scented Oil, Oil Oud, Vitamin E 100% Natural 1.0z 30ml Made in Uk i will have 5 types of oils Vanilla Oud Rose Oud Cocktail Tea Tree Velvet Beard Dusk Shampoo APPLICATION DIRECTIONS Massage into the beard / hair and rinse out with warm water. Distorted shampoos, there are no nasty chemicals which are damaging your beard instead of the wheat proteins and oils that you add to the hair follicles with nutrients and naturally adding a protective coating. INGREDIENTS Aqua (Water), Capryl / caprylyl glucoside, Cocomidopropyl betaine, Glycerin (Veg), Xanthan gum, Phenoxyethanol, Hydrolysed wheat protein, Aloe barbadensis (Aloe vera) leaf powder, Sodium benzoate, Potassium sorbate1 3.4 oz, 100ml Cylinder packaging for the Oils, Box for the shampoo
Nice to have
• I want "London" written underneath the logo and oil name.

```html
<!DOCTYPE html>
<html lang="en">
<head>
<meta charset="utf-8">
<title>Ashcroft Grooming – Beard Oil Label</title>
<link href="https://fonts.googleapis.com/css2?family=Quicksand:wght@500;600;700&display=swap" rel="stylesheet">
<style>
  :root {
    --canvas-bg: #f3f3f5;
    --label-black: #161616;
    --panel-black: #1b1b1b;
    --silver: #c9c9c9;
    --silver-dark: #6f6f6f;
    --gold: #d8b43a;
    --gold-deep: #b88c22;
    --text-light: #ececec;
  }
  * { box-sizing: border-box; margin: 0; padding: 0; }
  html, body {
    width: 1200px;
    height: 1200px;
    overflow: hidden;
    background: var(--canvas-bg);
  }
  .canvas {
    position: relative;
    width: 1200px;
    height: 1200px;
  }
  .label {
    position: absolute;
    left: 160px;
    top: 56px;
    width: 880px;
    height: 1088px;
    background: var(--label-black);
    overflow: hidden;
  }
  .label-pattern {
    position: absolute;
    inset: 18px 0;
    background:
      radial-gradient(ellipse at 50% 50%, rgba(20,20,20,0) 40%, rgba(120,120,120,0.18) 100%),
      linear-gradient(180deg, #262626 0%, #1a1a1a 50%, #262626 100%);
  }
  .silver-rule {
    position: absolute;
    left: 0;
    right: 0;
    height: 9px;
    background: linear-gradient(90deg, var(--silver-dark), var(--silver) 30%, #f0f0f0 55%, var(--silver) 80%, var(--silver-dark));
  }
  .silver-rule--top { top: 9px; }
  .silver-rule--bottom { bottom: 9px; }
  .info-panel {
    position: absolute;
    left: 112px;
    top: 180px;
    width: 630px;
    height: 712px;
    background: var(--panel-black);
    border: 9px solid var(--gold);
    box-shadow: inset 0 0 0 1px var(--gold-deep);
    display: flex;
    flex-direction: column;
    align-items: center;
    font-family: "Quicksand", sans-serif;
  }
  .brand-name {
    margin-top: 96px;
    display: flex;
    align-items: center;
    gap: 18px;
    color: var(--text-light);
    font-weight: 600;
    font-size: 58px;
    letter-spacing: 1px;
    line-height: 1;
  }
  .brand-mark {
    width: 22px;
    height: 22px;
    border-radius: 50%;
    background: var(--text-light);
  }
  .product-name {
    margin-top: 130px;
    color: var(--gold);
    font-weight: 500;
    font-size: 74px;
    line-height: 1;
  }
  .product-origin {
    margin-top: 150px;
    color: var(--gold);
    font-weight: 500;
    font-size: 50px;
    line-height: 1;
  }
  .product-volume {
    margin-top: 18px;
    color: var(--gold);
    font-weight: 500;
    font-size: 24px;
    line-height: 1;
  }
</style>
</head>
<body>
  <main class="canvas">
    <section class="label">
      <div class="label-pattern" role="img" aria-label="Silver zigzag line pattern surrounding the central panel"></div>
      <div class="silver-rule silver-rule--top"></div>
      <div class="silver-rule silver-rule--bottom"></div>
      <div class="info-panel">
        <div class="brand-name"><span class="brand-mark"></span>ASHCROFT GROOMING</div>
        <h1 class="product-name">Beard Oil</h1>
        <p class="product-origin">London</p>
        <p class="product-volume">100ml</p>
      </div>
    </section>
  </main>
</body>
</html>
```